Home Remodeling company needs a business card design

we need a business card design for home remodeling company in hamilton county, indiana USA. we offers a wide range of construction services including whole house renovations, Design and Build Basements and Kitchen and Bathroom Remodeling . we would like to see designs for both site of business card that use the same color of the company logo and also including all information below :
1- Samir Daoudi CEO / General Contractor
2- all company contacts Telephone numbers ( 1-888-TOVAL-42 ) ( 317-555-0192) email address ( info@tovalhome.example) website ( www.tovalhome.example ) and social media logos (Facebook- twitter- google plus )
3- company logo
4- licensed . insured . bonded

```html
<!DOCTYPE html>
<html lang="en">
<head>
<meta charset="UTF-8">
<title>Toval Home Remodeling – Business Card</title>
<link rel="stylesheet" href="https://fonts.googleapis.com/css2?family=Open+Sans:wght@400;600;700;800&display=swap">
<style>
  :root {
    --brand-red: #c4343b;
    --ink: #2f3033;
    --ink-soft: #3c3d40;
    --paper: #ffffff;
    --backdrop: #2a2c30;
  }
  * { margin: 0; padding: 0; box-sizing: border-box; }
  html, body {
    width: 1200px; height: 864px; overflow: hidden;
    background: var(--backdrop);
    font-family: "Open Sans", Arial, sans-serif;
  }
  .stage { position: relative; width: 1200px; height: 864px; }

  .card {
    position: absolute; left: 300px;
    width: 600px; height: 343px;
    overflow: hidden;
  }
  .card--front { top: 64px; background: var(--brand-red); color: var(--paper); }
  .card--back  { top: 455px; background: var(--paper); color: var(--ink); }

  /* Wordmark */
  .wordmark { position: absolute; display: flex; flex-direction: column; }
  .wordmark__row { display: flex; align-items: center; gap: 12px; }
  .wordmark__mark { width: 12px; height: 12px; }
  .wordmark__name { font-weight: 800; line-height: 1; letter-spacing: 2px; }
  .wordmark__tag { font-weight: 600; letter-spacing: 6px; line-height: 1; }

  .card--front .wordmark { left: 0; right: 0; top: 90px; align-items: center; }
  .card--front .wordmark__name { font-size: 72px; }
  .card--front .wordmark__mark { background: var(--paper); width: 14px; height: 14px; }
  .card--front .wordmark__tag { font-size: 19px; margin-top: 8px; padding-left: 50px; }

  .credentials {
    position: absolute; left: 0; right: 0; top: 268px;
    display: flex; align-items: center; gap: 14px;
  }
  .credentials__rule { flex: 1; height: 1px; background: rgba(255,255,255,0.85); }
  .credentials__text { font-size: 17px; font-weight: 600; letter-spacing: 0.3px; }

  .card--back .wordmark { left: 30px; top: 40px; }
  .card--back .wordmark__mark { background: var(--brand-red); }
  .card--back .wordmark__name { font-size: 46px; color: var(--ink); }
  .card--back .wordmark__tag { font-size: 13px; color: var(--ink-soft); margin-top: 5px; padding-left: 24px; letter-spacing: 5px; }

  .person { position: absolute; right: 26px; top: 124px; text-align: right; }
  .person__name { font-size: 17px; font-weight: 700; color: var(--brand-red); line-height: 22px; }
  .person__title { font-size: 14px; color: var(--ink); line-height: 20px; }

  .contacts {
    position: absolute; right: 26px; top: 178px;
    list-style: none; text-align: right;
  }
  .contacts__item {
    font-size: 14px; line-height: 21px; color: var(--ink);
    display: flex; align-items: center; justify-content: flex-end; gap: 8px;
  }
  .contacts__icon { width: 11px; height: 11px; fill: var(--brand-red); }

  .footer-band {
    position: absolute; left: 0; right: 0; bottom: 0; height: 70px;
    background: var(--brand-red);
  }
  .social {
    position: absolute; left: 225px; top: 50%; transform: translateY(-50%);
    display: flex; gap: 14px; list-style: none;
  }
  .social__dot {
    width: 28px; height: 28px; border-radius: 50%;
    border: 2px solid var(--paper);
    display: flex; align-items: center; justify-content: center;
  }
  .social__dot::after {
    content: ""; width: 18px; height: 18px; border-radius: 50%;
    background: var(--paper);
  }
</style>
</head>
<body>
<main class="stage">

  <section class="card card--front" aria-label="Card front">
    <div class="wordmark">
      <div class="wordmark__row">
        <span class="wordmark__mark"></span>
        <span class="wordmark__name">TOVAL</span>
      </div>
      <span class="wordmark__tag">HOME REMODELING</span>
    </div>
    <div class="credentials">
      <span class="credentials__rule"></span>
      <span class="credentials__text">Licensed . Insured . Bonded</span>
      <span class="credentials__rule"></span>
    </div>
  </section>

  <section class="card card--back" aria-label="Card back">
    <div class="wordmark">
      <div class="wordmark__row">
        <span class="wordmark__mark"></span>
        <span class="wordmark__name">TOVAL</span>
      </div>
      <span class="wordmark__tag">HOME REMODELING</span>
    </div>

    <div class="person">
      <p class="person__name">Samir Daoudi</p>
      <p class="person__title">CEO / General Contractor</p>
    </div>

    <ul class="contacts">
      <li class="contacts__item">1-888-TOVAL-42
        <svg class="contacts__icon" viewBox="0 0 24 24"><path d="M6.6 10.8a15.2 15.2 0 0 0 6.6 6.6l2.2-2.2a1 1 0 0 1 1-.25 11.4 11.4 0 0 0 3.6.57 1 1 0 0 1 1 1V20a1 1 0 0 1-1 1A17 17 0 0 1 3 4a1 1 0 0 1 1-1h3.5a1 1 0 0 1 1 1c0 1.25.2 2.45.57 3.57a1 1 0 0 1-.25 1z"/></svg>
      </li>
      <li class="contacts__item">317-555-0192
        <svg class="contacts__icon" viewBox="0 0 24 24"><path d="M6.6 10.8a15.2 15.2 0 0 0 6.6 6.6l2.2-2.2a1 1 0 0 1 1-.25 11.4 11.4 0 0 0 3.6.57 1 1 0 0 1 1 1V20a1 1 0 0 1-1 1A17 17 0 0 1 3 4a1 1 0 0 1 1-1h3.5a1 1 0 0 1 1 1c0 1.25.2 2.45.57 3.57a1 1 0 0 1-.25 1z"/></svg>
      </li>
      <li class="contacts__item">info@tovalhome.example
        <svg class="contacts__icon" viewBox="0 0 24 24"><path d="M2 5h20v14H2z M4 7v.4l8 5 8-5V7l-8 5z" fill-rule="evenodd"/></svg>
      </li>
      <li class="contacts__item">www.tovalhome.example
        <svg class="contacts__icon" viewBox="0 0 24 24"><path d="M10 14a4 4 0 0 1 0-5.6l3-3a4 4 0 0 1 5.6 5.6l-1.5 1.5-1.4-1.4 1.5-1.5a2 2 0 0 0-2.8-2.8l-3 3a2 2 0 0 0 0 2.8zm4-4a4 4 0 0 1 0 5.6l-3 3a4 4 0 0 1-5.6-5.6l1.5-1.5 1.4 1.4-1.5 1.5a2 2 0 0 0 2.8 2.8l3-3a2 2 0 0 0 0-2.8z"/></svg>
      </li>
    </ul>

    <div class="footer-band">
      <ul class="social" aria-label="Social media">
        <li class="social__dot" aria-label="Social profile 1"></li>
        <li class="social__dot" aria-label="Social profile 2"></li>
        <li class="social__dot" aria-label="Social profile 3"></li>
      </ul>
    </div>
  </section>

</main>
</body>
</html>
```